Website for UK Fintech Company specialising in Auto-Finance asset management

We need a website for a FINTECH business called KELVO Asset Management. We have developed and licenced an innovative platform to provide financial institutions whom provide secured Asset finance loans to consumer and commercial clients, allowing for real time tracking and management of defaulted accounts pending repossession. The KELVO Asset Management platform is a total recoveries solution through the cycle, from the moment the lender has to recover the vehicle (due to default/non-payment) to the disposal of the vehicle (via sale at Motor Auctions or by selling to a Car dealership network). The data provided from external services allows the Financier to make informed decisions, such as whether it is economical to continue the recovery and decide which sales channel is better suited for their assets to maximise residual values and minimise financial losses. The KELVO platform provides an array of MI reporting and uses a systematic approach utilising exception reporting to identify key areas of non-performance to enable focus where needed. KELVO also provides a leading Debt collection service recovering end-of-cycle losses such as Financial Shortfall and losses in vehicle values due to conditions and excessive damage.

We also require a new logo for out new product called PL-Certify

Target Market(s)

Financial institutions whom provide secured Asset finance loans to consumer and commercial clients

Industry/Entity Type

Financial Service

Logo Text

PL- Certify (this is for a new product which forms part of the KELVO Asset Mangement Platform

Number of Pages Required

4 page

Font styles to use
Serif
Sans Serif

Colors

Designer to choose colors to be used in the design.

Requirements
Must have
• We need a simple website with a broken down as follows;
• • Landing page
• • Services page
• • About us page
• • KELVO Asset Management Platform login page (client facing)
Nice to have
• Our slogan is 'Auto-Finance Expertise'
• We are very much open to suggestions as long as we can create a professional/ corporate / modern feel to the website. We are a FINTECH company, and that needs to come across
Should not have
• Whilst we are an asset management company primarily managing vehicles through our platform, we don't want it to look like a car dealership website!:)

```html
<!DOCTYPE html>
<html lang="en">
<head>
<meta charset="utf-8">
<title>PL-Certify — KELVO Asset Management</title>
<link rel="stylesheet" href="https://fonts.googleapis.com/css2?family=Montserrat:wght@400;500;600;700&family=Roboto:wght@300;400;500&display=swap">
<style>
:root{
  --orange:#f4800e;
  --orange-soft:#f7a043;
  --ink:#2b2b2b;
  --text:#3a3a3a;
  --muted:#8a8a8a;
  --teal:#3cbfae;
  --teal-dark:#2aa895;
  --rule:#e9e9e9;
  --accent-line:#ef6b6b;
  --white:#ffffff;
}
*{box-sizing:border-box;margin:0;padding:0}
html,body{width:1200px;height:2381px;overflow:hidden;background:var(--white)}
body{font-family:'Roboto',Arial,sans-serif;color:var(--text)}
.page{position:relative;width:1200px;height:2381px;overflow:hidden}
.abs{position:absolute}

/* header */
.site-header{position:absolute;left:0;top:0;width:1200px;height:49px;background:var(--white);border-bottom:1px solid var(--rule);z-index:3}
.brand{position:absolute;display:flex;align-items:center;gap:8px;font-family:'Montserrat',Arial,sans-serif;font-weight:700;color:var(--ink);letter-spacing:.2px}
.brand-mark{width:14px;height:14px;background:var(--orange)}
.site-header .brand{left:87px;top:8px;font-size:26px;line-height:32px}
.main-nav a{position:absolute;top:17px;font-family:'Roboto',Arial,sans-serif;font-size:13px;color:var(--text);text-decoration:none;letter-spacing:.4px}
.main-nav a.active{color:var(--ink)}
.main-nav a.active::after{content:"";position:absolute;left:0;right:0;bottom:-5px;height:2px;background:var(--orange)}
.login-btn{position:absolute;left:1028px;top:13px;width:84px;height:27px;background:var(--orange);border-radius:3px;color:var(--white);font-size:15px;display:flex;align-items:center;justify-content:center;gap:6px;text-decoration:none}

/* hero */
.hero{position:absolute;left:0;top:49px;width:1200px;height:522px;background:linear-gradient(100deg,#9fdcea 0%,#86e0e0 45%,#7be8df 100%)}
.hero-photo{position:absolute;left:587px;top:28px;width:540px;height:494px;background:radial-gradient(ellipse at 55% 45%,#e8c9b4 0%,#cfd9e6 45%,rgba(160,225,230,0) 75%)}
.hero-panel{position:absolute;left:0;top:256px;width:576px;height:223px;background:var(--orange-soft)}
.hero-title{position:absolute;left:87px;top:32px;width:460px;font-family:'Roboto',Arial,sans-serif;font-weight:500;font-size:25px;line-height:31px;letter-spacing:1.2px;color:var(--white);text-transform:uppercase}
.btn-ghost{position:absolute;left:87px;top:147px;width:137px;height:37px;border:1px solid var(--white);border-radius:3px;color:var(--white);font-family:'Montserrat',Arial,sans-serif;font-size:12px;display:flex;align-items:center;justify-content:center;letter-spacing:.4px}

/* section headings */
.section-title{position:absolute;left:0;width:1200px;text-align:center;font-family:'Montserrat',Arial,sans-serif;font-weight:700;font-size:27px;color:var(--ink);letter-spacing:.3px}
.section-title::after{content:"";display:block;width:46px;height:2px;background:var(--accent-line);margin:9px auto 0}

/* services */
.service{position:absolute;width:330px}
.service-icon{position:absolute;left:0;top:0;width:32px;height:32px}
.service h3{position:absolute;left:54px;top:0;font-family:'Roboto',Arial,sans-serif;font-weight:400;font-size:13px;color:var(--ink);letter-spacing:.3px;white-space:nowrap}
.service p{position:absolute;left:54px;top:22px;width:260px;font-size:13px;line-height:21px;color:var(--muted);font-weight:300}
.btn-solid{position:absolute;background:var(--orange);color:var(--white);border-radius:3px;font-family:'Montserrat',Arial,sans-serif;font-size:12px;display:flex;align-items:center;justify-content:center;letter-spacing:.4px}

/* about */
.about{position:absolute;left:0;top:1035px;width:1200px;height:473px;background:linear-gradient(90deg,#f6f6f6 0%,#f1ecea 35%,#f8f8f8 70%,#ffffff 100%);border-bottom:1px solid #dcdcdc}
.about-devices{position:absolute;left:140px;top:1103px;width:325px;height:440px;border-radius:26px;background:linear-gradient(160deg,#fafafa 0%,#e4e6ea 60%,#d5d8dd 100%);z-index:2}
.about-title{position:absolute;left:614px;top:1091px;font-family:'Montserrat',Arial,sans-serif;font-weight:700;font-size:27px;color:var(--ink)}
.about-title::after{content:"";display:block;width:46px;height:2px;background:var(--accent-line);margin-top:8px}
.about-copy{position:absolute;left:614px;width:500px;font-size:13.2px;line-height:21px;color:#222}

/* testimonial */
.testimonial-card{position:absolute;left:227px;top:1681px;width:738px;height:139px;border:1px solid #e4e4e4;border-radius:10px;background:var(--white)}
.quote-text{position:absolute;left:250px;top:1717px;width:692px;text-align:center;font-size:12.8px;line-height:21px;color:#555}
.avatar{position:absolute;left:455px;top:1793px;width:62px;height:62px;border-radius:50%;background:linear-gradient(150deg,#c98a6e,#9a5a44)}
.author-line{position:absolute;left:517px;top:1844px;width:58px;height:1px;background:#cfcfcf}
.author{position:absolute;left:579px;top:1834px;font-size:12.5px;color:#555}
.dots span{position:absolute;top:1912px;width:9px;height:9px;border-radius:50%;background:#c9c9c9}
.dots span.on{background:var(--accent-line)}

/* footer */
.site-footer{position:absolute;left:0;top:1989px;width:1200px;height:392px;background:linear-gradient(115deg,#8ad6c8 0%,#45bfae 40%,#2cad9c 100%);color:var(--ink)}
.site-footer .brand{left:87px;top:30px;font-size:26px}
.footer-about{position:absolute;left:87px;top:80px;width:290px;font-size:13.5px;line-height:21px;color:#1f2f2d}
.social a{position:absolute;top:2150px;width:36px;height:36px;border:1px solid #2d6c63;border-radius:50%}
.footer-heading{position:absolute;top:2014px;font-family:'Montserrat',Arial,sans-serif;font-weight:600;font-size:15px;letter-spacing:1px;color:#1f3431}
.quick-links a{position:absolute;left:519px;font-size:13px;color:#1f3431;text-decoration:none}
.field{position:absolute;left:748px;width:366px;background:var(--white);border-radius:3px;font-size:10px;color:#777;padding:8px 10px;letter-spacing:.4px}
.copyright{position:absolute;left:0;top:2350px;width:1200px;text-align:center;font-size:12px;color:#1f3431}
</style>
</head>
<body>
<div class="page">

  <header class="site-header">
    <div class="brand"><span class="brand-mark"></span>PL-Certify</div>
    <nav class="main-nav">
      <a href="#" class="active" style="left:452px">Home</a>
      <a href="#" style="left:575px">About Us</a>
      <a href="#" style="left:717px">Service</a>
      <a href="#" style="left:849px">Contact Us</a>
    </nav>
    <a href="#" class="login-btn">
      <svg width="10" height="12" viewBox="0 0 10 12"><rect x="1" y="5" width="8" height="7" rx="1" fill="#fff"/><path d="M3 5V3.5a2 2 0 0 1 4 0V5" stroke="#fff" stroke-width="1.4" fill="none"/></svg>
      Login
    </a>
  </header>

  <section class="hero" role="img" aria-label="Hero photograph of smiling clients on a light aqua background">
    <div class="hero-photo"></div>
    <div class="hero-panel">
      <h1 class="hero-title">Auto-finance expertise for real-time recovery and asset management.</h1>
      <div class="btn-ghost">VIEW MORE</div>
    </div>
  </section>

  <h2 class="section-title" style="top:625px">SERVICES</h2>

  <div class="service" style="left:98px;top:713px">
    <svg class="service-icon" viewBox="0 0 32 32" fill="none" stroke="#3cbfae" stroke-width="1.8"><path d="M16 29s-9-9.5-9-16a9 9 0 0 1 18 0c0 6.5-9 16-9 16z"/><circle cx="16" cy="13" r="3.5" fill="#3cbfae"/></svg>
    <h3>REAL-TIME TRACKING</h3>
    <p>Follow every defaulted account live, from default notice to repossession.</p>
  </div>
  <div class="service" style="left:451px;top:713px">
    <svg class="service-icon" viewBox="0 0 32 32" fill="none" stroke="#3cbfae" stroke-width="1.8"><path d="M26 12A11 11 0 0 0 6 10"/><path d="M6 4v6h6"/><path d="M6 20a11 11 0 0 0 20 2"/><path d="M26 28v-6h-6"/></svg>
    <h3>RECOVERY MANAGEMENT</h3>
    <p>Manage the full recoveries cycle, from vehicle collection to disposal.</p>
  </div>
  <div class="service" style="left:798px;top:713px">
    <svg class="service-icon" viewBox="0 0 32 32" fill="none" stroke="#3cbfae" stroke-width="1.8"><path d="M4 28h24"/><rect x="7" y="17" width="4" height="11" fill="#3cbfae"/><rect x="14" y="11" width="4" height="17"/><rect x="21" y="5" width="4" height="23" fill="#3cbfae"/></svg>
    <h3>MI REPORTING</h3>
    <p>An array of MI reports helps lenders make fast, informed decisions.</p>
  </div>
  <div class="service" style="left:98px;top:828px">
    <svg class="service-icon" viewBox="0 0 32 32" fill="none" stroke="#3cbfae" stroke-width="1.8"><path d="M4 16V5h11l13 13-11 11z"/><circle cx="10" cy="10" r="2.2" fill="#3cbfae"/></svg>
    <h3>REMARKETING CHANNELS</h3>
    <p>Sell via motor auction or dealer network to maximise residual values.</p>
  </div>
  <div class="service" style="left:451px;top:828px">
    <svg class="service-icon" viewBox="0 0 32 32" fill="none" stroke="#3cbfae" stroke-width="1.8"><path d="M16 4 29 27H3z"/><path d="M16 12v7"/><circle cx="16" cy="23" r="1.2" fill="#3cbfae"/></svg>
    <h3>EXCEPTION REPORTING</h3>
    <p>Spot key areas of non-performance and focus effort where it is needed.</p>
  </div>
  <div class="service" style="left:798px;top:828px">
    <svg class="service-icon" viewBox="0 0 32 32" fill="none" stroke="#3cbfae" stroke-width="1.8"><circle cx="16" cy="16" r="12"/><path d="M20 10.5a3.5 3.5 0 0 0-6.5 1.8V22M11 17h7M11 22h10"/></svg>
    <h3>DEBT COLLECTION</h3>
    <p>Recover end-of-cycle losses such as financial shortfall and damage.</p>
  </div>

  <div class="btn-solid" style="left:532px;top:935px;width:136px;height:36px">VIEW MORE</div>

  <section class="about" role="img" aria-label="Soft faded background photograph with light interface graphics"></section>
  <div class="about-devices" role="img" aria-label="Phone and tablet mock-ups showing the KELVO platform dashboard and mobile site"></div>
  <h2 class="about-title">ABOUT US</h2>
  <p class="about-copy" style="top:1160px">KELVO Asset Management is a UK fintech business. We have developed and licensed an innovative platform for financial institutions that provide secured asset finance loans to consumer and commercial clients. It allows real-time tracking and management of defaulted accounts pending repossession: a total recoveries solution from the moment a vehicle must be recovered to its sale at motor auction or through a dealer network.</p>
  <p class="about-copy" style="top:1307px">Data from external services shows whether it is economical to continue a recovery and which sales channel suits each asset best, helping lenders maximise residual values and minimise financial losses.</p>
  <div class="btn-solid" style="left:614px;top:1409px;width:137px;height:38px">READ MORE</div>

  <h2 class="section-title" style="top:1596px">TESTIMONIAL</h2>
  <div class="testimonial-card"></div>
  <svg class="abs" style="left:228px;top:1670px" width="34" height="26" viewBox="0 0 34 26" fill="#e3e3e3"><path d="M0 12h8v14H0zM0 12q0-10 12-12v4q-6 2-6 8zM18 12h8v14h-8zM18 12q0-10 12-12v4q-6 2-6 8z"/></svg>
  <svg class="abs" style="left:928px;top:1800px" width="34" height="26" viewBox="0 0 34 26" fill="#e3e3e3"><g transform="rotate(180 17 13)"><path d="M0 12h8v14H0zM0 12q0-10 12-12v4q-6 2-6 8zM18 12h8v14h-8zM18 12q0-10 12-12v4q-6 2-6 8z"/></g></svg>
  <p class="quote-text">The KELVO platform has given our recoveries team real-time visibility of every defaulted account. Exception reporting shows us exactly where to focus, and the choice of sales channels has helped us lift residual values and reduce losses across our portfolio.</p>
  <div class="avatar" role="img" aria-label="Portrait photo of the reviewer"></div>
  <div class="author-line"></div>
  <div class="author">Jane Doe ,&nbsp; Head of Recoveries</div>
  <div class="dots"><span class="on" style="left:571px"></span><span style="left:594px"></span><span style="left:617px"></span></div>

  <footer class="site-footer">
    <div class="brand"><span class="brand-mark"></span>PL-Certify</div>
    <p class="footer-about">Part of the KELVO Asset Management platform: auto-finance expertise from vehicle recovery to disposal.</p>
  </footer>
  <div class="social">
    <a href="#" aria-label="Social profile 1" style="left:87px"></a>
    <a href="#" aria-label="Social profile 2" style="left:141px"></a>
    <a href="#" aria-label="Social profile 3" style="left:196px"></a>
    <a href="#" aria-label="Social profile 4" style="left:250px"></a>
    <a href="#" aria-label="Social profile 5" style="left:304px"></a>
  </div>
  <h4 class="footer-heading" style="left:516px">QUICK LINKS</h4>
  <nav class="quick-links">
    <a href="#" style="top:2046px">Home</a>
    <a href="#" style="top:2088px">About Us</a>
    <a href="#" style="top:2130px">Service</a>
    <a href="#" style="top:2172px">Contact Us</a>
  </nav>
  <h4 class="footer-heading" style="left:748px">CONTACT US</h4>
  <div class="field" style="top:2050px;height:31px">NAME</div>
  <div class="field" style="top:2093px;height:32px">EMAIL</div>
  <div class="field" style="top:2138px;height:119px">MESSAGE</div>
  <div class="btn-solid" style="left:748px;top:2270px;width:130px;height:36px;font-weight:600">SEND MESSAGE</div>
  <p class="copyright">© 2018. PL- Certify. All Rights Reserved.</p>

</div>
</body>
</html>
```